High School brochure for an international high school

Innovative and colorful school brochure appealing to an international market.
Please incorporate all the content provided in the Word document attached.
The logo files are attached with a white and a blue background. Use the whole logo with the text or logo only depending upon the page used.

The snippet below is from the Word document provided. Please refer to the Word document for more:
Online American High School * Grades 6 – 12

A unique school
• Differentiated Education
• College Prep Curriculum
• Flexible programs
• Promoting intellectual maturity and responsibility
• Global Peer learning

A learning environment for all
• Gifted students
• Students engaged in significant pursuits in the areas of sports, arts, etc.
• Home schoolers
• English Language Learners
• Accelerating postsecondary completion through Scholar Track® (ST®)* courses

Pictures 1, 2,3

Vision Statement

Brightvale Institute is a premier American online high school offering comprehensive, collaborative, and affordable learning to a diverse and intellectually passionate global community.

Mission Statement

Brightvale Institute provides high-quality, flexible, individualized educational experiences in a safe, technology-enabled learning environment to empower students to achieve their academic and personal goals.

Academics

Brightvale Institute’s differentiated curriculum with project based learning at its core fosters critical reasoning and argumentation while engaging students in advanced academic content. Students work closely with the instructors in a peer-learning environment that motivates them to reach their full academic potential.

Students are placed in courses based on ability, not age or grade level, and he academic plans are tailored for each student that will prepare them for success in the future - college and beyond.

The curriculum includes Project Based Inquiry courses where students take part in learning experiences framed around answering Big Questions or addressing Big Challenges that guide instruction and serve to organize their learning progressions. As students pursue answers, they conduct investigations, make models, collect and analyze data, weigh evidence, write explanations, and discuss and present findings, a process that empowers students with STEM.

From middle school through high school, students are introduced to various aspects of competitive testing. Tests and quizzes that reflect college entrance tests like QRT and LMX are embodied into the curriculum that helps students develop deeper analytical skills.

Highlights: (Individual items To be used in highlighted boxes across the brochure)

• Award-winning courseware proven by third-party research and studies
• Inquiry-based learning – develop student knowledge towards solutions
• Our students can challenge themselves with ST* Courses
• Peer learning - mutually beneficial and involve the sharing of knowledge, ideas and experience across a global community
• Self Organized Learning Environment – Learn to Learn
• Personalized college counseling and planning
• Tutoring plans

Target Market(s)

High School students and parents

Industry/Entity Type

Education

Font styles to use
Sans Serif

Requirements
Must have
• Adobe Indesign file delivery
• Innovative, colorful and high school appeal
• Use images from http://brightvaleinstitute.org as these images have already been purchased.
• Use your own images, icons as appropriate to the content
• Minimum of 4 pages and maximum of 8 pages (all pages in A4 size)
Nice to have
• Idea inspirations are included in the document
• Please contact us if you have any questions about the content.
• Improvise/create highlight material as needed from the content provided
• You can also use content from our website.

```html
<!DOCTYPE html>
<html lang="en">
<head>
<meta charset="utf-8">
<title>Brightvale Institute – Mission Statement</title>
<link rel="stylesheet" href="https://fonts.googleapis.com/css2?family=Oswald:wght@500;600&family=Open+Sans:wght@400;600&family=Cormorant+Garamond:ital,wght@1,500&display=swap">
<style>
  :root {
    --navy: #1f3a6b;
    --navy-deep: #17305c;
    --orange: #f08a24;
    --sky: #8fb0dc;
    --paper: #ffffff;
    --mist: #eef1f6;
    --ink: #ffffff;
    --leaf-light: #c9d48a;
    --leaf-mid: #8c9a3f;
    --bark: #5b4a33;
    --book-red: #a5392e;
    --book-cream: #e9dcc0;
  }
  * { box-sizing: border-box; margin: 0; padding: 0; }
  html, body { width: 851px; height: 1200px; overflow: hidden; background: var(--paper); }
  .page { position: relative; width: 851px; height: 1200px; background: var(--paper); overflow: hidden; }

  .masthead { position: absolute; left: 0; top: 0; width: 851px; height: 128px; background: var(--paper); }
  .masthead-bands { position: absolute; left: 0; top: 0; }
  .brand { position: absolute; left: 0; right: 0; top: 34px; display: flex; justify-content: center; align-items: center; gap: 16px; }
  .brand-mark { width: 46px; height: 46px; background: var(--navy); border-radius: 50%; }
  .brand-name { font-family: "Oswald", sans-serif; font-weight: 500; font-size: 40px; letter-spacing: 3px; color: var(--navy); text-transform: uppercase; }

  .hero-photo { position: absolute; left: 0; top: 128px; width: 851px; height: 440px;
    background: radial-gradient(ellipse at 45% 30%, var(--leaf-light) 0%, var(--leaf-mid) 45%, var(--bark) 100%); }

  .highlight-card { position: absolute; left: 624px; top: 142px; width: 147px; height: 438px; background: var(--navy); }
  .highlight-card .dot { position: absolute; width: 56px; height: 56px; border-radius: 50%; background: var(--mist); border: 3px solid var(--sky); }
  .highlight-card .dot.top { left: -14px; top: 22px; }
  .highlight-card .dot.bottom { right: -14px; bottom: 22px; }
  .highlight-text { position: absolute; left: 14px; right: 14px; top: 120px; font-family: "Cormorant Garamond", serif; font-style: italic; font-weight: 500; font-size: 25px; line-height: 1.15; color: var(--ink); text-align: center; }

  .mission { position: absolute; left: 91px; top: 624px; width: 334px; height: 510px; background: var(--navy-deep); }
  .mission-squares { position: absolute; right: 22px; top: 12px; display: flex; gap: 8px; }
  .mission-squares span { width: 24px; height: 24px; background: var(--sky); border-radius: 3px; }
  .mission-band { position: absolute; left: 16px; right: 0; top: 34px; height: 118px; background: var(--orange); padding: 8px 18px; }
  .mission-title { font-family: "Oswald", sans-serif; font-weight: 600; color: var(--ink); text-transform: uppercase; line-height: 1; }
  .mission-title .big { display: block; font-size: 60px; letter-spacing: 1px; }
  .mission-title .small { display: block; font-size: 38px; letter-spacing: 1px; margin-top: 2px; }
  .mission-copy { position: absolute; left: 28px; right: 24px; top: 190px; font-family: "Open Sans", sans-serif; font-size: 17px; line-height: 1.5; color: var(--ink); text-align: center; }

  .tutoring-photo { position: absolute; left: 425px; top: 638px; width: 298px; height: 496px;
    background: linear-gradient(180deg, var(--mist) 0%, var(--book-cream) 35%, var(--book-red) 75%, var(--bark) 100%); }
  .tutoring-caption { position: absolute; left: 425px; top: 1060px; width: 298px; height: 74px; display: flex; align-items: center; gap: 12px; padding-left: 44px; }
  .tutoring-caption .dot { width: 50px; height: 50px; border-radius: 50%; background: var(--mist); border: 3px solid var(--sky); }
  .tutoring-caption p { font-family: "Cormorant Garamond", serif; font-style: italic; font-weight: 500; font-size: 26px; color: var(--navy); }
</style>
</head>
<body>
<div class="page">
  <header class="masthead">
    <svg class="masthead-bands" width="200" height="128" viewBox="0 0 200 128" aria-hidden="true">
      <polygon points="0,0 175,0 105,50 0,50" fill="#f08a24"/>
      <polygon points="0,50 105,50 40,100 0,100" fill="#1f3a6b"/>
    </svg>
    <div class="brand">
      <span class="brand-mark"></span>
      <span class="brand-name">Brightvale Institute</span>
    </div>
  </header>

  <div class="hero-photo" role="img" aria-label="Looking up a tall tree trunk into a sunlit green and golden canopy"></div>

  <aside class="highlight-card">
    <span class="dot top"></span>
    <p class="highlight-text">Award-winning courseware proven by third-party research and studies</p>
    <span class="dot bottom"></span>
  </aside>

  <section class="mission">
    <div class="mission-squares"><span></span><span></span></div>
    <div class="mission-band">
      <h2 class="mission-title"><span class="big">Mission</span><span class="small">Statement</span></h2>
    </div>
    <p class="mission-copy">Brightvale Institute provides high-quality, flexible, individualized educational experiences in a safe, technology-enabled learning environment to empower students to achieve their academic and personal goals.</p>
  </section>

  <div class="tutoring-photo" role="img" aria-label="A tall stack of colourful hardcover books"></div>
  <div class="tutoring-caption">
    <span class="dot"></span>
    <p>Tutoring plans</p>
  </div>
</div>
</body>
</html>
```